Fundraising Study Day East of England. Lift the January blues!

A flyer to advertise a fundraising event of lectures for dental hygienists and therapists in support of the exemption campaign. Currently dental hygienists and therapists require a prescription to deliver certain treatment or recommend certain toothpastes. If we are successful in the campaign we will be able to treat patients without these restrictions.

Industry/Entity Type

Dental

```html
<!DOCTYPE html>
<html lang="en">
<head>
<meta charset="utf-8">
<title>Fundraising Study Day East of England</title>
<link rel="stylesheet" href="https://fonts.googleapis.com/css2?family=Montserrat:wght@600;700;800&family=PT+Sans:ital,wght@0,400;0,700;1,700&display=swap">
<style>
:root{
  --page:#f2f2f3;
  --paper:#e9e9eb;
  --navy:#2c5687;
  --navy-deep:#244b78;
  --sky:#3ab5df;
  --ink:#222428;
  --white:#ffffff;
}
*{box-sizing:border-box;margin:0;padding:0}
html,body{width:1200px;height:1166px;overflow:hidden;background:var(--page)}
.flyer{
  position:absolute;left:194px;top:14px;width:943px;height:1323px;
  transform:scale(0.86);transform-origin:0 0;
  background:linear-gradient(90deg,#ececee 0%,#e6e6e8 60%,#ececee 100%);
  overflow:hidden;font-family:"PT Sans",Arial,sans-serif;
}
.top-rule{position:absolute;left:0;top:0;width:100%;height:12px;background:linear-gradient(90deg,var(--navy-deep),#3b6898)}
.portrait{
  position:absolute;left:530px;top:43px;width:413px;height:1118px;z-index:0;
  background:linear-gradient(180deg,#e4e4e6 0%,#f4f4f5 25%,#f7f7f8 55%,#2a2a2c 62%,#121214 100%);
}
.headline{position:absolute;left:0;top:30px;width:556px;text-align:center;font-family:"Montserrat",Arial,sans-serif;z-index:1}
.headline h1{font-size:54px;line-height:65px;font-weight:700;color:var(--sky);letter-spacing:1px}
.headline h2{font-size:38px;line-height:46px;font-weight:800;color:var(--navy-deep);margin-top:-2px;letter-spacing:.5px}
.description{position:absolute;left:23px;top:290px;width:477px;z-index:1}
.description h3{text-align:center;font-size:27px;font-weight:700;color:var(--navy-deep);line-height:34px}
.description p{font-size:17.4px;line-height:22.7px;color:var(--navy);text-align:justify;text-align-last:center}
.date-panel{
  position:absolute;left:14px;top:476px;width:494px;height:92px;z-index:1;
  background:linear-gradient(90deg,#2b5383,#3a6696);color:var(--white);
  font-family:"Montserrat",Arial,sans-serif;font-weight:700;text-align:center;
}
.date-panel .date{font-size:23px;margin-top:15px}
.date-panel .date sup{font-size:13px}
.date-panel .venue{font-size:17.5px;margin-top:8px;display:flex;align-items:center;justify-content:center;gap:10px}
.info-band{
  position:absolute;left:14px;top:581px;width:526px;height:60px;z-index:1;
  background:linear-gradient(90deg,#3290c4,var(--sky) 60%);
  clip-path:polygon(0 0,96% 0,100% 100%,0 100%);
  color:var(--white);font-family:"Montserrat",Arial,sans-serif;font-weight:700;font-size:18.5px;
  display:flex;align-items:center;
}
.info-band .item{display:flex;align-items:center;gap:12px}
.info-band .time{margin-left:22px}
.info-band .price{margin-left:38px}
.agenda{position:absolute;left:14px;top:652px;width:508px;z-index:1}
.agenda h4{font-size:21px;font-weight:700;color:var(--navy-deep);display:inline-block;padding-bottom:3px;border-bottom:2px solid var(--navy-deep);margin-bottom:12px}
.agenda p{font-size:15.6px;line-height:20.4px;color:var(--ink)}
.agenda .slot{color:var(--navy-deep);font-weight:700}
.agenda .pause{color:var(--navy-deep);font-weight:700;font-style:italic}
.booking{
  position:absolute;left:0;top:1161px;width:100%;height:162px;z-index:2;
  background:linear-gradient(90deg,#2b5383,#3b6797 50%,#2b5383);
  color:var(--white);text-align:center;
}
.booking h5{font-family:"Montserrat",Arial,sans-serif;font-weight:700;font-size:27px;letter-spacing:.5px;margin-top:22px}
.booking .rule{width:400px;height:3px;margin:4px auto 0;background:linear-gradient(90deg,transparent,#dfe8f2,transparent)}
.booking .url{font-size:24.5px;font-weight:700;line-height:33px;margin-top:18px}
</style>
</head>
<body>
<article class="flyer">
  <div class="top-rule"></div>
  <div class="portrait" role="img" aria-label="Photo of a smiling professional woman in a white blouse and black skirt, arms folded"></div>

  <header class="headline">
    <h1>Fundraising<br>Study Day East<br>of England.</h1>
    <h2>Lift the January blues!</h2>
  </header>

  <section class="description">
    <h3>DESCRIPTION</h3>
    <p>A fundraising event to support our exemptions project. The day will consist of a series of presentations ranging from the new ECPD to new technologies. The aim, being to enhance our learning and raise funds to support the exemptions campaign. The speaker line includes some of the UK and Irelands most respected dental professionals in our field.</p>
  </section>

  <div class="date-panel">
    <div class="date">On Friday 19<sup>th</sup> January, 2018</div>
    <div class="venue">
      <svg width="18" height="24" viewBox="0 0 18 24"><path d="M9 0C4 0 0 4 0 9c0 6.5 9 15 9 15s9-8.5 9-15c0-5-4-9-9-9z" fill="#fff"/><circle cx="9" cy="9" r="3.4" fill="#2c5687"/></svg>
      Harrow Lane Hotel, Mill Road, Stanford SG9 4QT
    </div>
  </div>

  <div class="info-band">
    <div class="item time">
      <svg width="40" height="40" viewBox="0 0 40 40"><circle cx="20" cy="20" r="17.5" fill="none" stroke="#fff" stroke-width="3"/><path d="M20 9v11l7 6" fill="none" stroke="#fff" stroke-width="3" stroke-linecap="round"/></svg>
      09:00 – 16:30 (GMT)
    </div>
    <div class="item price">
      <svg width="38" height="38" viewBox="0 0 38 38"><path d="M21 3h13v13L17 33 5 21z" fill="none" stroke="#fff" stroke-width="2.5" stroke-linejoin="round"/><circle cx="28" cy="9" r="2.3" fill="#fff"/><path d="M16 23l6-6" stroke="#fff" stroke-width="2"/></svg>
      £101.48 Only
    </div>
  </div>

  <section class="agenda">
    <h4>Agenda</h4>
    <p>
      <span class="slot">9.30 - 10.15</span><br>
      Helen Marsh: Immediate past president of the DTGA will be updating us on all things ECPD<br>
      <span class="slot">10.15 - 11.00</span><br>
      Clara Whitby: Will provide an update on teeth whiteing and explain how social media has impacted her business<br>
      Natalie Greaves: Our internationally acclaimed speaker will update our knowledge of periodontal disease and nutrition and new technologies.<br>
      <span class="pause">11.00 - 11.30 Break</span><br>
      <span class="slot">11.30 - 13.00</span><br>
      Orla Brennan &amp; Tessa Holloway: Will be providing a combined presentation on 'Scaling your business' and start to finish UltraFlow techniques. The aim being to build our business with effective communications, systems and protocols. This sessions promises audience participation!<br>
      <span class="pause">12.00 - 14.00 lunch</span><br>
      <span class="slot">14.00 - 15.00</span><br>
      Ravi Desai: Save your back. All things posture.<br>
      <span class="pause">15.00 - 15.30 Break</span><br>
      <span class="slot">15.30 -16.30</span><br>
      Natalie Greaves: Our internationally acclaimed speaker will update our knowledge of periodontal disease and nutrition and new technologies.
    </p>
  </section>

  <footer class="booking">
    <h5>BOOK YOUR TICKETS HERE</h5>
    <div class="rule"></div>
    <p class="url">https://www.ticketsquare.co.uk/e/fundraising-study-day-east-of<br>-england-lift-the-january-blues-tickets-48210357</p>
  </footer>
</article>
</body>
</html>
```